Harborline Equipment Alliance Business Card Redesign

Logo has already been developed. The current business card is one sided. We'd like our mission on the back and more creativity so it pops. We may also like a tagline on the back
One call...all the service, all the savings. Examples are attached from our printer but we don't like them. The front is how we have our existing cards but the back is new. We are open to all ideas. We do like our colors/ brand of purple, black, white...

```html
<!DOCTYPE html>
<html lang="en">
<head>
<meta charset="utf-8">
<title>Harborline Equipment Alliance – Business Card</title>
<link rel="stylesheet" href="https://fonts.googleapis.com/css2?family=Questrial&family=Arimo:wght@400;700&display=swap">
<style>
  :root {
    --stage: #2b2b2d;
    --card-dark: #3a3a3c;
    --card-light: #efefef;
    --purple: #5b2a86;
    --purple-soft: #7a45a8;
    --ink: #2a2a2a;
    --white: #f4f4f4;
    --muted: #b9b9bb;
  }
  * { margin: 0; padding: 0; box-sizing: border-box; }
  html, body { width: 1200px; height: 800px; overflow: hidden; }
  body {
    background: var(--stage);
    position: relative;
    font-family: "Questrial", sans-serif;
  }
  .card {
    position: absolute;
    top: 240px;
    width: 540px;
    height: 310px;
    border-radius: 22px;
    overflow: hidden;
    background: var(--card-dark);
    box-shadow: 0 14px 30px rgba(0,0,0,.45);
  }
  .card--front { left: 45px; }
  .card--back { left: 615px; }
  .card__shapes { position: absolute; inset: 0; }
  .abs { position: absolute; }

  /* front */
  .brand-name {
    left: 30px; top: 38px;
    font-family: "Questrial", sans-serif;
    font-size: 26px; color: var(--ink);
  }
  .company { left: 175px; top: 42px; }
  .company__name {
    font-family: "Arimo", sans-serif; font-weight: 700;
    font-size: 19px; color: var(--purple);
  }
  .company__tagline {
    font-family: "Arimo", sans-serif; font-weight: 700;
    font-size: 15px; color: var(--ink); margin-top: 2px;
  }
  .contacts {
    left: 30px; top: 200px;
    color: var(--muted); font-size: 12.5px; line-height: 17px;
  }
  .contacts__row { display: flex; align-items: flex-start; gap: 8px; }
  .contacts__row + .contacts__row { margin-top: 6px; }
  .contacts svg { flex: none; margin-top: 2px; }
  .person { right: 30px; top: 214px; text-align: right; }
  .person__name {
    font-family: "Arimo", sans-serif; font-weight: 700;
    font-size: 20px; color: var(--white); letter-spacing: 1px;
  }
  .person__title { font-size: 15px; color: var(--muted); margin-top: 2px; }
  .person__email {
    margin-top: 10px; font-size: 13px; color: var(--muted);
    display: flex; align-items: center; justify-content: flex-end; gap: 7px;
  }

  /* back */
  .back-name {
    left: 0; right: 0; top: 92px; text-align: center;
    font-size: 30px; color: var(--card-light);
  }
  .back-tagline {
    left: 0; right: 0; top: 170px; text-align: center;
    font-size: 18px; color: var(--white); letter-spacing: .5px;
  }
  .back-mission {
    left: 70px; right: 70px; top: 212px; text-align: center;
    font-size: 13px; line-height: 19px; color: var(--muted);
  }
</style>
</head>
<body>

<section class="card card--front" aria-label="Business card front">
  <svg class="card__shapes" width="540" height="310" viewBox="0 0 540 310" aria-hidden="true">
    <polygon points="0,0 540,0 540,198 0,132" fill="var(--card-light)"/>
    <polygon points="0,138 540,204 540,213 0,147" fill="var(--purple)"/>
    <polygon points="402,185 428,188 414,202" fill="var(--card-light)" stroke="var(--purple)" stroke-width="2"/>
  </svg>

  <div class="abs brand-name">Harborline</div>
  <div class="abs company">
    <div class="company__name">Harborline Equipment Alliance</div>
    <div class="company__tagline">Delivering Results. Creating Savings.</div>
  </div>

  <div class="abs contacts">
    <div class="contacts__row">
      <svg width="12" height="12" viewBox="0 0 12 12"><path d="M2.5 1h2l1 3-1.3 1a6 6 0 0 0 2.8 2.8l1-1.3 3 1v2c0 .6-.4 1-1 1A9.5 9.5 0 0 1 1.5 2c0-.6.4-1 1-1z" fill="var(--purple-soft)"/></svg>
      <div>(555) 210-4410<br>(555) 210-4482<br>(555) 377-0915</div>
    </div>
    <div class="contacts__row">
      <svg width="12" height="12" viewBox="0 0 12 12"><path d="M6 0.5a4 4 0 0 1 4 4c0 3-4 7-4 7s-4-4-4-7a4 4 0 0 1 4-4zm0 2.5a1.5 1.5 0 1 0 0 3 1.5 1.5 0 0 0 0-3z" fill="var(--purple-soft)"/></svg>
      <div>1840 W. Harbor Avenue<br>Suite 200, Portland, OR 97209</div>
    </div>
  </div>

  <div class="abs person">
    <div class="person__name">DANA WHITFIELD</div>
    <div class="person__title">Business Development Manager</div>
    <div class="person__email">
      <svg width="13" height="10" viewBox="0 0 13 10"><rect x="0.5" y="0.5" width="12" height="9" rx="1" fill="var(--purple-soft)"/><path d="M1 1l5.5 4.5L12 1" fill="none" stroke="var(--card-dark)" stroke-width="1.2"/></svg>
      <span>dwhitfield@HarborlineAlliance.com</span>
    </div>
  </div>
</section>

<section class="card card--back" aria-label="Business card back">
  <div class="abs back-name">Harborline Equipment Alliance</div>
  <p class="abs back-tagline">One Call. All the Service. All the Savings.</p>
  <p class="abs back-mission">Built on honest advice and hard work, we earn lasting client loyalty.</p>
</section>

</body>
</html>
```